Motor Insurance Quotation - New Quote format / New Template

We are a 40 year old insurance company called 'Velmor Insurance Agency L.L.C' in Dubai, UAE (Our logo / color design can and details can be found on www.velmorgulf.example).

Velmor provides all kinds of insurance solutions for its clients...currently is this modern fast paced world of ever changing technology and increasing competition we need to be ahead of our competitors...

In order to do so, we are in need to re-design our motor insurance quotation format / template and require it to be more attractive, modern and professional.
Since it is a text heavy format, we need it to look aesthetically appealing to our clients.

We would like to see designs that use our color code (as our website / sample quote currently used is attached)..these designs are required in pdf illustrator formats....i have also attached quotation formats used in the existing market. the template and the samples are only for reference and the templates are not to be followed.

UAE

Insurance

• arial

• Aesthetic Design, Insurance details and covers provided in our quote, Velmor logo, color code (details can be found on our website)
• 1 page (short quote) and 2 page (detailed quote) designs to shared...

```html
<!DOCTYPE html>
<html lang="en">
<head>
<meta charset="utf-8">
<title>Velmor Motor Quotation Template</title>
<link href="https://fonts.googleapis.com/css2?family=Arimo:wght@400;700&display=swap" rel="stylesheet">
<style>
:root{
  --purple:#7b2d8e;
  --navy:#16237a;
  --bg:#e4e4e4;
  --paper:#ffffff;
  --soft:#f1f1f1;
  --row:#ececec;
  --ink:#4a4a4a;
  --meta:#7f8fb3;
}
*{margin:0;padding:0;box-sizing:border-box}
html,body{width:1200px;height:1200px;overflow:hidden;background:var(--bg)}
body{font-family:"Arimo",Arial,sans-serif}
.board{position:absolute;left:0;top:0;width:1500px;height:1500px;transform:scale(.8);transform-origin:0 0}
.board-title{position:absolute;top:92px;left:0;width:1500px;text-align:center;font-size:68px;font-weight:400;color:var(--purple);letter-spacing:1px}
.page{position:absolute;top:275px;width:689px;height:965px;background:var(--paper);box-shadow:0 6px 14px rgba(0,0,0,.25);overflow:hidden}
.page--quote{left:36px}
.page--auth{left:775px}
.header-art,.footer-art{position:absolute;left:0}
.header-art{top:0}
.footer-art{top:885px}
.brand{position:absolute;left:21px;top:16px;font-size:43px;font-weight:400;color:var(--navy);letter-spacing:1px}
.doc-title{position:absolute;left:0;height:26px;width:320px;background:var(--soft);font-size:9px;font-weight:700;color:var(--navy);line-height:26px;padding-left:19px}
.doc-title::after{content:"";position:absolute;right:-32px;top:0;width:6px;height:26px;background:var(--navy);transform:skewX(-45deg)}
.sec{position:absolute;left:44px;width:601px}
.band{position:relative;height:16px;line-height:16px;font-size:9px;color:var(--purple);text-align:center}
.band::before{content:"";position:absolute;top:0;bottom:0;left:8px;right:8px;border:1px solid var(--purple);border-left:5px solid var(--purple);transform:skewX(-45deg)}
.band span{position:relative}
.band--navy{color:var(--navy)}
.band--navy::before{border-color:var(--navy)}
.band-row{display:flex}
.band-row .band{flex:1}
.band-row .band+.band{margin-left:-10px}
.rows{margin-top:1px}
.row{display:flex;height:15px;line-height:15px;font-size:9px;color:var(--ink);text-align:center}
.row:nth-child(odd){background:var(--row)}
.row>div{border-right:2px solid var(--paper);white-space:nowrap;overflow:hidden}
.row>div:last-child{border-right:0}
.k{width:218px}
.v{flex:1}
.c3{width:200px}
.c3:last-child{flex:1}
.note{position:absolute;left:44px;width:601px;text-align:center;font-size:7.4px;font-weight:700;line-height:9px}
.note--purple{color:var(--purple)}
.note--navy{color:var(--navy)}
.office{position:absolute;left:36px;top:880px;color:var(--navy);font-size:9.5px;font-weight:700;line-height:11px}
.office-name{font-size:14px;color:var(--purple);line-height:17px;margin-bottom:2px}
.office svg{width:8px;height:8px;vertical-align:-1px;margin-right:2px;fill:var(--purple)}
.office .gap{display:inline-block;width:10px}
.reg{position:absolute;left:487px;top:897px;font-size:5.6px;font-weight:700;color:var(--meta);line-height:7.2px}
.lbl{position:absolute;left:44px;width:166px}
.field{position:absolute;left:212px;width:433px;height:15px;background:var(--row)}
.boxes{position:absolute;left:212px;display:flex;align-items:center;height:17px;font-size:9px;font-weight:700;color:var(--purple)}
.box{width:18px;height:15px;background:var(--row);margin-right:4px}
.boxes .grp{margin-right:6px}
.boxes em{font-style:normal;margin:0 8px 0 2px}
.sign-area{position:absolute;left:44px;top:663px;width:601px;height:50px;background:var(--soft)}
.aed{position:absolute;left:44px;top:542px;width:601px;height:16px;background:var(--soft);font-size:9px;font-weight:700;color:var(--purple);line-height:16px;padding-left:5px}
</style>
</head>
<body>
<main class="board">
  <h1 class="board-title">REVISED DESIGN.</h1>

  <!-- Quotation page -->
  <section class="page page--quote">
    <svg class="header-art" width="689" height="76" viewBox="0 0 689 76">
      <polygon points="0,0 245,0 180,64 0,64" fill="#f1f1f1"/>
      <line x1="246" y1="0" x2="182" y2="64" stroke="#d6d6d6"/>
      <polygon points="372,0 689,0 689,18 354,18" fill="#f1f1f1"/>
      <line x1="372" y1="18" x2="345" y2="46" stroke="#cfcfcf"/>
      <line x1="372" y1="18" x2="689" y2="18" stroke="#d6d6d6"/>
      <polygon points="288,46 348,46 340,55 280,55" fill="#7b2d8e"/>
      <polygon points="362,46 689,46 689,55 353,55" fill="#7b2d8e"/>
      <polygon points="0,69 266,69 260,75 0,75" fill="#7b2d8e"/>
    </svg>
    <div class="brand">VELMOR</div>
    <div class="doc-title" style="top:83px">MOTOR COMPREHENSIVE, FIRE, THEFT &amp; THIRD PARTY LIABILITY</div>

    <div class="sec" style="top:126px">
      <div class="band-row">
        <div class="band"><span>Quote Reference</span></div>
        <div class="band band--navy"><span><b>MVA/2016/00603OM</b></span></div>
        <div class="band"><span>Date of Issue</span></div>
        <div class="band band--navy"><span><b>12/01/2017</b></span></div>
      </div>
    </div>

    <div class="sec" style="top:150px">
      <div class="band"><span>Driver Details</span></div>
      <div class="rows">
        <div class="row"><div class="k">Insured Name</div><div class="v">Leena Farouk</div></div>
        <div class="row"><div class="k">Address</div><div class="v">Dubai</div></div>
        <div class="row"><div class="k">Phone Number</div><div class="v">L.Farouk@mailbox.example</div></div>
        <div class="row"><div class="k">Email</div><div class="v">050-0001234</div></div>
        <div class="row"><div class="k">Age</div><div class="v">26 Years</div></div>
      </div>
    </div>

    <div class="sec" style="top:245px">
      <div class="band"><span>Vehicle Details</span></div>
      <div class="rows">
        <div class="row"><div class="k">Make</div><div class="v">Korvan</div></div>
        <div class="row"><div class="k">Model</div><div class="v">K16</div></div>
        <div class="row"><div class="k">Year of Make</div><div class="v">2011</div></div>
        <div class="row"><div class="k">Seating Capacity</div><div class="v">5</div></div>
        <div class="row"><div class="k">Body</div><div class="v">Saloon</div></div>
      </div>
    </div>

    <div class="sec" style="top:342px">
      <div class="band"><span>Type of Cover</span></div>
      <div class="rows">
        <div class="row"><div class="v">Comprehensive, Fire, Theft &amp; Third Party Liability</div></div>
      </div>
    </div>

    <div class="sec" style="top:382px">
      <div class="band"><span>Quote Details</span></div>
      <div class="rows">
        <div class="row"><div class="k">Sum Insured</div><div class="v">AED 40,000.00</div></div>
        <div class="row"><div class="k">Premium</div><div class="v">AED 1,740.00</div></div>
        <div class="row"><div class="k">Excess</div><div class="v">AED 350.00</div></div>
      </div>
    </div>

    <div class="sec" style="top:449px">
      <div class="band-row">
        <div class="band"><span>Cover</span></div>
        <div class="band band--navy"><span>Coverage / Cost</span></div>
        <div class="band"><span>Limit</span></div>
      </div>
      <div class="rows">
        <div class="row"><div class="c3">Personal Accident Benefits for Driver</div><div class="c3">Included</div><div class="c3">AED 200,000</div></div>
        <div class="row"><div class="c3">Personal Accident Benefits for Passengers</div><div class="c3">Included</div><div class="c3">AED 200,000 per Passenger</div></div>
        <div class="row"><div class="c3">Premier Roadside Assistance - Silver Card</div><div class="c3">Included</div><div class="c3">Unlimited (Once every 24 hours)</div></div>
        <div class="row"><div class="c3">Premier Roadside Assistance - Gold Card</div><div class="c3">Optional / AED 100</div><div class="c3" style="font-size:8px">Registration Service &amp; Off Road Pull Out (8am to</div></div>
        <div class="row"><div class="c3">Rent a Car Option</div><div class="c3">Optional / AED 250</div><div class="c3">3 times per year, 10 days each</div></div>
        <div class="row"><div class="c3">Agency Repairs</div><div class="c3">Excluded</div><div class="c3">-</div></div>
        <div class="row"><div class="c3">Off Road Cover</div><div class="c3">Excluded</div><div class="c3">Excess AED 750</div></div>
        <div class="row"><div class="c3">Orange Card</div><div class="c3">Optional / Tariff Attached</div><div class="c3">-</div></div>
        <div class="row"><div class="c3">Territorial Limits</div><div class="c3">Included</div><div class="c3">UAE</div></div>
        <div class="row"><div class="c3">Third Party Bodily Injury</div><div class="c3">Included</div><div class="c3">Unlimited</div></div>
        <div class="row"><div class="c3">Third Party Property Damage</div><div class="c3">Included</div><div class="c3">AED 5,000,000</div></div>
        <div class="row"><div class="c3">Ambulance Cover</div><div class="c3">Included</div><div class="c3">-</div></div>
        <div class="row"><div class="c3">Windscreen Claims</div><div class="c3">Included</div><div class="c3">Excess will apply</div></div>
        <div class="row"><div class="c3">Medical Expenses</div><div class="c3">Included</div><div class="c3">AED 10,000 / Person</div></div>
        <div class="row"><div class="c3">Personal Effects(Theft subject to forcible entry)</div><div class="c3">Included</div><div class="c3">AED 4,000</div></div>
        <div class="row"><div class="c3">Natural Calamities</div><div class="c3">Included</div><div class="c3">-</div></div>
      </div>
    </div>

    <p class="note note--purple" style="top:718px">Where the insured requests the replacement of the damaged parts with new parts, the insured shall bear the rates of depreciation i.e. nil for brand new vehicles, 5% for the 2nd year, 10% for the 3rd year, 15% for the 4th year, 20% for the 5th year and a maximum of 30% for the 6th year onwards.</p>
    <p class="note note--navy" style="top:746px">An Excess of 10% (besides the normal excess) of the amount of the accident is applicable for drivers who are less than 25 years of age<br>This insurance is non transferrable</p>

    <div class="sec" style="top:774px">
      <div class="band"><span>Should you accept the above terms, kindly provide us with the following:</span></div>
    </div>

    <div class="sec" style="top:798px">
      <div class="band-row">
        <div class="band" style="flex:2"><span>New Client</span></div>
        <div class="band band--navy"><span>Existing Client</span></div>
      </div>
      <div class="rows">
        <div class="row"><div class="c3">Passport &amp; Visa Copy</div><div class="c3">Financing Bank name, if any</div><div class="c3">Registration Card / Purchase Agreement Copy</div></div>
        <div class="row"><div class="c3">Driving License copy</div><div class="c3">Mobile Number &amp; P.O. Box Number</div><div class="c3">Financing Bank name, if any</div></div>
        <div class="row"><div class="c3">Registration Card / Purchase Agreement Copy</div><div class="c3">Attached Credit Form Copy</div><div class="c3">Attached Credit Form Copy</div></div>
      </div>
    </div>

    <svg class="footer-art" width="689" height="80" viewBox="0 0 689 80">
      <rect x="480" y="0" width="209" height="52" fill="#f1f1f1"/>
      <rect x="0" y="7" width="476" height="3" fill="#7b2d8e"/>
      <polygon points="318,52 689,52 689,62 308,62" fill="#7b2d8e"/>
      <polygon points="306,64 689,64 689,80 292,80" fill="#7b2d8e"/>
    </svg>
    <div class="office">
      <div class="office-name">Velmor Dubai</div>
      <div>Harbour View Street, Crescent Business Bldg.</div>
      <div><svg viewBox="0 0 10 10"><path d="M5 0a3.5 3.5 0 0 0-3.5 3.5C1.5 6 5 10 5 10s3.5-4 3.5-6.5A3.5 3.5 0 0 0 5 0zm0 5a1.5 1.5 0 1 1 0-3 1.5 1.5 0 0 1 0 3z"/></svg>P.O.Box 4020, Dubai, UAE</div>
      <div><svg viewBox="0 0 10 10"><path d="M2 0l2 2.5-1 1.3a6 6 0 0 0 3.2 3.2l1.3-1L10 8 8.5 10C4 10 0 6 0 1.5z"/></svg>+971 4 000 1100<span class="gap"></span><svg viewBox="0 0 10 10"><path d="M2 0h5v3H2zM0 4h10v6H0zm2 2v1h2V6zm4 0v1h2V6z"/></svg>+971 4 000 1155</div>
      <div><svg viewBox="0 0 10 10"><circle cx="5" cy="5" r="4.3" fill="none" stroke="#7b2d8e" stroke-width="1.2"/><path d="M.7 5h8.6M5 .7v8.6" stroke="#7b2d8e" stroke-width="1"/></svg>www.velmorgulf.example<span class="gap"></span><svg viewBox="0 0 10 10"><path d="M0 1.5h10v7H0zm1 1L5 5.5 9 2.5" stroke="#fff" stroke-width=".8"/></svg>info@velmorgulf.example</div>
    </div>
    <div class="reg">Registered name: Velmor Insurance Agency L.L.C<br>General Agents for Al Sahil National Insurance Co. (PSC)<br>Insurance Agents Registration No. 18<br>A member of the Velmor Insurance Group</div>
  </section>

  <!-- Credit card authorisation page -->
  <section class="page page--auth">
    <svg class="header-art" width="689" height="76" viewBox="0 0 689 76">
      <polygon points="0,0 245,0 180,64 0,64" fill="#f1f1f1"/>
      <line x1="246" y1="0" x2="182" y2="64" stroke="#d6d6d6"/>
      <polygon points="372,0 689,0 689,18 354,18" fill="#f1f1f1"/>
      <line x1="372" y1="18" x2="345" y2="46" stroke="#cfcfcf"/>
      <line x1="372" y1="18" x2="689" y2="18" stroke="#d6d6d6"/>
      <polygon points="288,46 348,46 340,55 280,55" fill="#7b2d8e"/>
      <polygon points="362,46 689,46 689,55 353,55" fill="#7b2d8e"/>
      <polygon points="0,69 266,69 260,75 0,75" fill="#7b2d8e"/>
    </svg>
    <div class="brand">VELMOR</div>
    <div class="doc-title" style="top:171px;width:170px">CREDIT CARD AUTHORISATION</div>

    <div class="lbl band" style="top:214px"><span>Name of the Insured</span></div><div class="field" style="top:215px"></div>
    <div class="lbl band" style="top:237px"><span>Policy / Invoice Number</span></div><div class="field" style="top:238px"></div>
    <div class="lbl band" style="top:260px"><span>Mobile / Telephone No</span></div><div class="field" style="top:261px"></div>
    <div class="lbl band" style="top:283px"><span>(Mandatory) Email ID</span></div><div class="field" style="top:284px"></div>

    <div class="lbl band" style="top:333px"><span>CARD TYPE A</span></div><div class="boxes" style="top:333px"><div class="box"></div></div>
    <div class="lbl band" style="top:356px"><span>CARD TYPE B</span></div><div class="boxes" style="top:356px"><div class="box"></div></div>

    <div class="lbl band" style="top:405px"><span>Credit Card number</span></div>
    <div class="boxes" style="top:405px">
      <div class="box"></div><div class="box"></div><div class="box"></div><div class="box grp"></div>
      <div class="box"></div><div class="box"></div><div class="box"></div><div class="box grp"></div>
      <div class="box"></div><div class="box"></div><div class="box"></div><div class="box grp"></div>
      <div class="box"></div><div class="box"></div><div class="box"></div><div class="box"></div>
    </div>
    <div class="lbl band" style="top:428px"><span>Expiry Date</span></div>
    <div class="boxes" style="top:428px"><div class="box"></div><div class="box"></div><em>MM</em><div class="box"></div><div class="box"></div><em>YY</em></div>
    <div class="lbl band" style="top:452px"><span>CVV</span></div>
    <div class="boxes" style="top:452px"><div class="box"></div><div class="box"></div><div class="box"></div></div>
    <div class="lbl band" style="top:475px"><span>Name as on the Credit Card</span></div><div class="field" style="top:476px"></div>

    <div class="sec" style="top:524px"><div class="band"><span>I confirm that the payment is being made by me in respect of my policy for the amount of</span></div></div>
    <div class="aed">AED</div>

    <div class="lbl band" style="top:592px"><span>Date</span></div>
    <div class="boxes" style="top:592px"><div class="box"></div><div class="box"></div><em>DD</em><div class="box"></div><div class="box"></div><em>MM</em><div class="box"></div><div class="box"></div><em>YY</em></div>

    <div class="sec" style="top:645px"><div class="band"><span>Cardholders Name &amp; Signature</span></div></div>
    <div class="sign-area"></div>

    <p class="note note--purple" style="top:754px;font-size:8.6px;line-height:10px;font-weight:400">Please note the by completing these payment details you are implicitly accepting the purchase of the<br>insurance policy for the amount specified above.</p>

    <svg class="footer-art" width="689" height="80" viewBox="0 0 689 80">
      <rect x="480" y="0" width="209" height="52" fill="#f1f1f1"/>
      <rect x="0" y="7" width="476" height="3" fill="#7b2d8e"/>
      <polygon points="318,52 689,52 689,62 308,62" fill="#7b2d8e"/>
      <polygon points="306,64 689,64 689,80 292,80" fill="#7b2d8e"/>
    </svg>
    <div class="office">
      <div class="office-name">Velmor Dubai</div>
      <div>Harbour View Street, Crescent Business Bldg.</div>
      <div><svg viewBox="0 0 10 10"><path d="M5 0a3.5 3.5 0 0 0-3.5 3.5C1.5 6 5 10 5 10s3.5-4 3.5-6.5A3.5 3.5 0 0 0 5 0zm0 5a1.5 1.5 0 1 1 0-3 1.5 1.5 0 0 1 0 3z"/></svg>P.O.Box 4020, Dubai, UAE</div>
      <div><svg viewBox="0 0 10 10"><path d="M2 0l2 2.5-1 1.3a6 6 0 0 0 3.2 3.2l1.3-1L10 8 8.5 10C4 10 0 6 0 1.5z"/></svg>+971 4 000 1100<span class="gap"></span><svg viewBox="0 0 10 10"><path d="M2 0h5v3H2zM0 4h10v6H0zm2 2v1h2V6zm4 0v1h2V6z"/></svg>+971 4 000 1155</div>
      <div><svg viewBox="0 0 10 10"><circle cx="5" cy="5" r="4.3" fill="none" stroke="#7b2d8e" stroke-width="1.2"/><path d="M.7 5h8.6M5 .7v8.6" stroke="#7b2d8e" stroke-width="1"/></svg>www.velmorgulf.example<span class="gap"></span><svg viewBox="0 0 10 10"><path d="M0 1.5h10v7H0zm1 1L5 5.5 9 2.5" stroke="#fff" stroke-width=".8"/></svg>info@velmorgulf.example</div>
    </div>
    <div class="reg">Registered name: Velmor Insurance Agency L.L.C<br>General Agents for Al Sahil National Insurance Co. (PSC)<br>Insurance Agents Registration No. 18<br>A member of the Velmor Insurance Group</div>
  </section>
</main>
</body>
</html>
```